Soy Candle Labels

We sell soy candles in recycled wine bottles. The wine bottle is cut in half and filled with pure and natural soy wax and scented with essential oils.
Our product represents good use of up cycling materials for a better use. The product is all natural and eco friendly.
You can see good use of labels and branding for a company in America that does the same thing http://marrowlanewicks.example/
Trya dn keep the label uncomplicated like the above labels.
We will need an area to hand stamp the scent. Similar to the labels used on the above website.
We would prefer to use a white or off white paper label with gold or bronze printing - limit the use of colour and keep the label simple and sophisticated.
Brambrel Candle Co. is our company name. Brambrel being the predominant name and candle co. written small underneath right justified.
Die cut labels might look better than a rectangle.
Dimensions should be 90mm Wide x 90mm High
The final design should communicate a professional and quality product. But stay modern and professional. Clean, elegant and sophisticated.
Can use wording such as: Hand Poured, Premium Soy Wax, All Natural, Up cycled
Have a look at the attached image for the look and feel we are going for.
Updates
Designers are having a little bit of trouble interpreting the brief into a viable design. To assist perhaps you can look at WINE LABELS on google images. Design your label around an existing style wine label to give the canld ethe feel of being a bottle of wine. Get creative! :)
Reason: We require more designs. We havnt quite got what were looking for.
Please see brief.

```html
<!DOCTYPE html>
<html lang="en">
<head>
<meta charset="utf-8">
<title>Brambrel Candle Co. – Soy Candle Label</title>
<link rel="stylesheet" href="https://fonts.googleapis.com/css2?family=Allura&family=Cormorant+SC:wght@500;600&display=swap">
<style>
  :root {
    --page: #ffffff;
    --label-cream: #f6ecde;
    --panel-cream: #f8efe3;
    --ornament-fill: #e3d6b2;
    --ink-gold: #9a8752;
  }
  html, body {
    margin: 0;
    padding: 0;
    width: 948px;
    height: 1200px;
    overflow: hidden;
    background: var(--page);
  }
  .label {
    position: relative;
    width: 948px;
    height: 1200px;
  }
  .label-art {
    position: absolute;
    inset: 0;
    width: 948px;
    height: 1200px;
  }
  .brand-name {
    position: absolute;
    left: 0;
    width: 948px;
    top: 548px;
    margin: 0;
    text-align: center;
    font-family: "Allura", cursive;
    font-weight: 400;
    font-size: 170px;
    line-height: 1;
    color: var(--ink-gold);
  }
  .brand-sub {
    position: absolute;
    right: 232px;
    top: 708px;
    margin: 0;
    font-family: "Cormorant SC", serif;
    font-weight: 500;
    font-size: 44px;
    line-height: 1;
    letter-spacing: 3px;
    color: var(--ink-gold);
  }
  .claims {
    position: absolute;
    left: 0;
    width: 948px;
    top: 856px;
    margin: 0;
    text-align: center;
    font-family: "Cormorant SC", serif;
    font-weight: 600;
    font-size: 32px;
    line-height: 52px;
    letter-spacing: 3px;
    color: var(--ink-gold);
  }
</style>
</head>
<body>
<main class="label">
  <svg class="label-art" viewBox="0 0 443 561" preserveAspectRatio="none">
    <defs>
      <linearGradient id="gold-stroke" x1="0" y1="0" x2="1" y2="1">
        <stop offset="0" stop-color="#c9b57f"/>
        <stop offset="0.45" stop-color="#8a7745"/>
        <stop offset="0.7" stop-color="#d6c693"/>
        <stop offset="1" stop-color="#7d6c3e"/>
      </linearGradient>
      <radialGradient id="center-glow" cx="0.5" cy="0.5" r="0.5">
        <stop offset="0" stop-color="#ffffff"/>
        <stop offset="0.55" stop-color="#fbf6ee"/>
        <stop offset="1" stop-color="#f8efe3" stop-opacity="0"/>
      </radialGradient>
      <linearGradient id="crest-tone" x1="0" y1="0" x2="0" y2="1">
        <stop offset="0" stop-color="#cdbb88"/>
        <stop offset="1" stop-color="#8f7d4b"/>
      </linearGradient>
    </defs>

    <path class="die-cut" fill="var(--label-cream)"
      d="M 221 116 C 150 118 90 140 30 146 Q 14 148 14 164 L 14 190 Q 4 196 4 210 L 4 370 Q 4 384 14 390 L 14 440 Q 14 456 30 458 C 90 464 150 486 221 488 C 292 486 352 464 413 458 Q 429 456 429 440 L 429 390 Q 439 384 439 370 L 439 210 Q 439 196 429 190 L 429 164 Q 429 148 413 146 C 352 140 292 118 221 116 Z"/>

    <path class="crest" role="img" aria-label="Fan-shaped shell crest ornament" fill="url(#crest-tone)"
      d="M 180 121 Q 184 80 221 66 Q 258 80 262 121 Q 241 115 221 115 Q 201 115 180 121 Z"/>

    <path class="panel" fill="var(--panel-cream)"
      d="M 221 128 C 150 130 100 150 30 158 L 30 422 C 100 430 150 468 221 472 C 292 468 342 430 413 422 L 413 158 C 342 150 292 130 221 128 Z"/>

    <circle class="sunburst" role="img" aria-label="Soft radiating sunburst behind the name" cx="221" cy="300" r="165" fill="url(#center-glow)"/>

    <path class="frame" fill="none" stroke="url(#gold-stroke)" stroke-width="3.5"
      d="M 221 128 C 150 130 100 150 30 158 L 30 422 C 100 430 150 468 221 472 C 292 468 342 430 413 422 L 413 158 C 342 150 292 130 221 128 Z"/>
    <path class="frame-inner" fill="none" stroke="url(#gold-stroke)" stroke-width="1.2"
      d="M 221 136 C 152 138 104 158 38 165 L 38 415 C 104 423 152 460 221 464 C 290 460 338 423 405 415 L 405 165 C 338 158 290 138 221 136 Z"/>

    <g class="corner-scrolls" fill="var(--ornament-fill)">
      <circle role="img" aria-label="Gold scroll flourish, top left" cx="50" cy="180" r="20"/>
      <circle role="img" aria-label="Gold scroll flourish, top right" cx="393" cy="180" r="20"/>
      <circle role="img" aria-label="Gold scroll flourish, bottom left" cx="50" cy="405" r="20"/>
      <circle role="img" aria-label="Gold scroll flourish, bottom right" cx="393" cy="405" r="20"/>
    </g>

    <ellipse class="deco-ornament" role="img" aria-label="Art deco fan and scroll ornament above the name" cx="221" cy="180" rx="56" ry="32" fill="var(--ornament-fill)"/>
  </svg>

  <h1 class="brand-name">Brambrel</h1>
  <p class="brand-sub">Candle Co.</p>
  <p class="claims">Hand Poured<br>Premium Soy Wax</p>
</main>
</body>
</html>
```